Maple Dental of Temecula needs a flyer

We need a flyer design for Maple Dental. We are located in the city of Linden Valley in California. Our dental office does general dentistry, cosmetic dentistry, dental implants, orthodontics, dental sleep apnea and TMJ treatment. We would like to design a flyer that could allow the reader know about our services and let them know that we accept new patients. We also have a new patient special that would included necessary dental x rays and dental exam for only $65. We do accept all major credit cards. Also our office accepts most PPO insurances. You can use some of the photos that are included or use stock photos of the dental procedure (they could be before/after photos).

```html
<!DOCTYPE html>
<html lang="en">
<head>
<meta charset="utf-8">
<title>Maple Dental – Flyer</title>
<link rel="stylesheet" href="https://fonts.googleapis.com/css2?family=Source+Sans+3:wght@400;600;700;800&display=swap">
<style>
  :root {
    --maroon: #5a3742;
    --charcoal: #414141;
    --mist: #e4e4e6;
    --white: #ffffff;
    --ink: #1c1c1c;
    --body: #333333;
  }
  html, body { margin: 0; padding: 0; overflow: hidden; background: var(--white); }
  .flyer {
    position: relative;
    width: 849px; height: 1200px;
    overflow: hidden;
    background: var(--white);
    font-family: "Source Sans 3", "Source Sans Pro", Arial, sans-serif;
    color: var(--ink);
  }
  .block { position: absolute; }
  .corner-grey { left: 554px; top: 0; width: 295px; height: 160px; background: var(--mist); }
  .rule-dark { left: 312px; top: 160px; width: 537px; height: 14px; background: var(--charcoal); }
  .side-grey { left: 0; top: 176px; width: 184px; height: 108px; background: var(--mist); }
  .right-grey { left: 554px; top: 284px; width: 295px; height: 43px; background: var(--mist); }

  .brand { position: absolute; left: 51px; top: 26px; }
  .brand-name { margin: 0; font-size: 47px; font-weight: 700; letter-spacing: 0.5px; line-height: 1; color: var(--ink); }
  .brand-doctor { margin: 5px 0 0; font-size: 18px; font-weight: 700; letter-spacing: 0.4px; line-height: 1; color: var(--ink); }
  .brand-tagline { margin: 5px 0 0; font-size: 23px; font-weight: 400; color: var(--maroon); line-height: 1.1; }

  .welcome {
    position: absolute; left: 194px; top: 174px; width: 655px; height: 110px;
    background: var(--maroon); color: var(--white);
    box-sizing: border-box; padding: 20px 0 0 14px;
    font-size: 29px; font-weight: 600; line-height: 1.28;
  }
  .welcome p { margin: 0; }

  .office-photo {
    position: absolute; left: 0; top: 327px; width: 554px; height: 375px;
    background: linear-gradient(160deg, #c9a46b 0%, #8a6a45 35%, #4b3a2a 70%, #2e2420 100%);
  }
  .special {
    position: absolute; left: 554px; top: 405px; width: 295px; height: 297px;
    background: var(--charcoal); color: var(--white);
    box-sizing: border-box; padding: 46px 10px 0 27px;
    font-size: 24px; line-height: 1.22; font-weight: 400;
  }
  .special p { margin: 0; }

  .results {
    position: absolute; left: 0; top: 702px; width: 849px; height: 162px;
    background: linear-gradient(90deg, #3b2e28 0%, #4a3a30 67%, var(--charcoal) 67.4%);
  }
  .result-photo { position: absolute; top: 0; height: 126px; width: 201px; }
  .result-photo.decay { left: 10px; background: linear-gradient(135deg, #d76a4c, #b8453a 60%, #e2c79a); }
  .result-photo.restored { left: 219px; background: linear-gradient(135deg, #c9a27a, #e6d2a8 50%, #b06a52); }
  .result-photo.gap { left: 432px; background: linear-gradient(135deg, #d5d3c6, #b9b6a8 55%, #7a3a30); }
  .result-photo.smile { left: 641px; background: linear-gradient(135deg, #c64a3c, #e7d3a4 50%, #c84b3d); }
  .result-label { position: absolute; top: 134px; font-size: 17px; color: var(--white); }

  .doctor-photo {
    position: absolute; left: 0; top: 864px; width: 295px; height: 336px;
    background: linear-gradient(180deg, #f3f3f3 0%, #e9e9e9 55%, #2a2a2e 100%);
  }

  .offer-title {
    position: absolute; left: 357px; top: 886px; margin: 0;
    font-size: 54px; font-weight: 800; letter-spacing: 0.5px; color: var(--maroon); line-height: 1;
  }
  .services {
    position: absolute; left: 346px; top: 958px; width: 500px;
    margin: 0; padding: 0; list-style: none;
    display: grid; grid-template-columns: 256px 244px; row-gap: 13px;
    font-size: 25.5px; color: var(--body); line-height: 1.25;
  }

  .contact-rule { left: 376px; top: 1104px; width: 473px; height: 10px; background: var(--charcoal); }
  .contact {
    position: absolute; left: 295px; top: 1114px; width: 554px; height: 86px;
    background: var(--maroon); color: var(--white); font-size: 17px;
  }
  .contact-item { position: absolute; display: flex; align-items: center; gap: 9px; white-space: nowrap; }
  .contact-item svg { width: 24px; height: 24px; flex: none; }
  .address { left: 45px; top: 11px; }
  .phone { left: 45px; top: 46px; }
  .email { left: 253px; top: 46px; }
</style>
</head>
<body>
<main class="flyer">
  <div class="block corner-grey"></div>
  <div class="block rule-dark"></div>
  <div class="block side-grey"></div>
  <div class="block right-grey"></div>

  <header class="brand">
    <h1 class="brand-name">MAPLE DENTAL</h1>
    <p class="brand-doctor">DANIEL MARSH, DDS, MAGD</p>
    <p class="brand-tagline">Where Healthy Smiles Take Shape</p>
  </header>

  <section class="welcome">
    <p>Welcome to Maple Dental. We are located<br>in the city of Linden Valley in California.</p>
  </section>

  <div class="office-photo" role="img" aria-label="Photo of the dental office waiting room with green chairs, a coffee table and a wall screen"></div>

  <section class="special">
    <p>Our new patient special includes a dental x rays and dental exam for only $65. We do accept all major credit cards. Also our office accepts most PPO insurances.</p>
  </section>

  <section class="results">
    <div class="result-photo decay" role="img" aria-label="Before photo: decayed teeth"></div>
    <div class="result-photo restored" role="img" aria-label="After photo: restored teeth"></div>
    <div class="result-photo gap" role="img" aria-label="Before photo: smile with a missing front tooth"></div>
    <div class="result-photo smile" role="img" aria-label="After photo: complete restored smile"></div>
    <span class="result-label" style="left:11px">Before</span>
    <span class="result-label" style="left:224px">After</span>
    <span class="result-label" style="left:434px">Before</span>
    <span class="result-label" style="left:648px">After</span>
  </section>

  <div class="doctor-photo" role="img" aria-label="Portrait of the dentist in a dark suit and tie"></div>

  <h2 class="offer-title">WHAT WE OFFER</h2>
  <ul class="services">
    <li>- General Dentistry</li>
    <li>- Cosmetic Dentistry</li>
    <li>- Dental Implants</li>
    <li>- Orthodontics</li>
    <li>- Dental Sleep Apnea</li>
    <li>- TMJ Treatment</li>
  </ul>

  <div class="block contact-rule"></div>
  <footer class="contact">
    <div class="contact-item address">
      <svg viewBox="0 0 24 24" aria-hidden="true">
        <circle cx="12" cy="12" r="11" fill="#fff"/>
        <path d="M6 12.2 12 7l6 5.2M8 11v6h3v-3.5h2V17h3v-6" fill="none" stroke="#5a3742" stroke-width="1.8" stroke-linejoin="round"/>
      </svg>
      <span>18420 Orchard Vista Road #210 Linden Valley CA 90999</span>
    </div>
    <div class="contact-item phone">
      <svg viewBox="0 0 24 24" aria-hidden="true">
        <circle cx="12" cy="12" r="11" fill="#fff"/>
        <path d="M8.3 6.5c.5-.4 1.2-.3 1.5.2l1.2 2c.3.5.2 1-.2 1.4l-.8.6c.6 1.4 1.6 2.5 3 3.2l.7-.8c.4-.4 1-.5 1.4-.2l2 1.2c.5.3.6 1 .2 1.5l-.9 1c-.6.6-1.5.8-2.300.5-3.2-1.2-5.6-3.6-6.8-6.8-.3-.8-.1-1.7.5-2.3z" fill="#5a3742"/>
      </svg>
      <span>(555) 014-2287</span>
    </div>
    <div class="contact-item email">
      <svg viewBox="0 0 24 24" aria-hidden="true">
        <circle cx="12" cy="12" r="11" fill="#fff"/>
        <rect x="6.5" y="8" width="11" height="8" rx="1" fill="#5a3742"/>
        <path d="M6.8 8.4 12 12.6l5.2-4.2" fill="none" stroke="#fff" stroke-width="1.1"/>
      </svg>
      <span>office@maple-dental.com</span>
    </div>
  </footer>
</main>
</body>
</html>
```